Allied Health team of Physiotherapists & Occupational Therapists seek a business card design

We have our new logo, we now need our new business cards and stationary. Blossom: Lymphoedema & Women's Clinic is seeking a generic card design to represent our whole team and individual cards for each therapist that incorporates our new logo to communicate our holistic approach that is calming, nuturing, supportive and welcoming.
Our Physiotherapists and Occupational Therapists assess, treat and provide education for people who are at risk of or who have lymphoedema. This is often as a result of treatment for cancer. We provide pre-operative and post-operative management and cancer rehabilitation in our Pilates studio. Our team also consists of Physiotherapists who have a strong interest in pelvic floor and continence management for both men and women.

Target Market(s)

Mainly women health conscious

Industry/Entity Type

Allied Health: Physiotherapy / Occupational Therapy

Contact Information for Business Card

Address: 14 Calloway Ave Bayhaven 3201 Phone: 84317560 fax: 8431 7564 Email: info@blossomcarepartners.com.au Website: blossomcarepartners.com.au Facebook address: facebook.com/BlossomLymphoedemaAndWomensCareCentre. Room to write appointments. Individual cards need to have name, office email and individual email and professional details

Requirements
Must have
• Logo as per uploaded documents

```html
<!DOCTYPE html>
<html lang="en">
<head>
<meta charset="utf-8">
<title>Blossom – Business Cards</title>
<link rel="stylesheet" href="https://fonts.googleapis.com/css2?family=Marcellus&family=Roboto:ital,wght@0,400;1,400&family=Source+Sans+3:wght@400;700&display=swap">
<style>
  :root {
    --backdrop: #2e2e30;
    --card: #f4f4f3;
    --ink: #222222;
    --muted: #3a3a3a;
    --accent: #d98c60;
    --accent-light: #e49d72;
    --band-text: #fbeee6;
  }
  * { box-sizing: border-box; margin: 0; padding: 0; }
  html, body { width: 1200px; height: 1138px; overflow: hidden; }
  body {
    background: var(--backdrop);
    position: relative;
    font-family: "Roboto", sans-serif;
    color: var(--ink);
  }
  .card {
    position: absolute;
    width: 622px;
    height: 375px;
    background: var(--card);
    border-radius: 16px;
    overflow: hidden;
  }
  .card--appointment { left: 274px; top: 186px; }
  .card--contact { left: 276px; top: 608px; }

  .brand {
    position: absolute;
    display: flex;
    align-items: center;
    gap: 8px;
    font-family: "Marcellus", serif;
    color: var(--accent);
  }
  .brand__dot {
    width: 12px; height: 12px; border-radius: 50%;
    background: var(--accent);
  }
  .card--appointment .brand { right: 26px; top: 70px; font-size: 30px; }
  .card--contact .brand { left: 70px; top: 164px; font-size: 42px; }

  .appointment__title {
    position: absolute; left: 26px; top: 56px;
    font-family: "Marcellus", serif;
    font-size: 30px; color: var(--accent); font-weight: 400;
    -webkit-text-stroke: 0.4px var(--accent);
  }
  .appointment__form {
    position: absolute; left: 25px; right: 25px; top: 152px;
    font-size: 18px;
  }
  .form-row {
    display: flex; align-items: flex-end; gap: 6px;
    height: 29px;
  }
  .form-row__blank {
    border-bottom: 1.3px solid var(--ink);
    height: 19px;
  }
  .form-row__blank--grow { flex: 1; }
  .form-row__blank--entry { width: 272px; }
  .form-row__blank--date { width: 91px; }
  .form-row__blank--time { width: 90px; }
  .form-row__label--date { margin-left: 4px; }
  .form-row__label--time { margin-left: 4px; }

  .appointment__notice {
    position: absolute; left: 0; right: 0; bottom: 0; height: 66px;
    background: linear-gradient(90deg, var(--accent), var(--accent-light));
    color: var(--band-text);
    font-family: "Source Sans 3", sans-serif;
    font-size: 14.5px; line-height: 21px;
    padding: 12px 30px 0 37px;
  }
  .appointment__notice strong { font-weight: 700; color: #fff; }

  .contact__details { position: absolute; left: 295px; top: 76px; }
  .contact__name {
    font-family: "Marcellus", serif; font-size: 23px;
    color: var(--accent); font-weight: 400; line-height: 28px;
    -webkit-text-stroke: 0.4px var(--accent);
  }
  .contact__role { font-style: italic; font-size: 16px; line-height: 21px; color: var(--muted); margin-top: 2px; }
  .contact__specialty { font-size: 16px; line-height: 21px; color: var(--muted); }
  .contact__list { list-style: none; margin-top: 30px; font-size: 17px; color: var(--ink); }
  .contact__list li { display: flex; align-items: center; gap: 12px; height: 26px; }
  .contact__list svg { width: 15px; height: 15px; fill: var(--accent); flex: none; }
  .contact__phone-pair { display: flex; gap: 22px; }
  .contact__phone-pair span { display: flex; align-items: center; gap: 12px; }
</style>
</head>
<body>

<section class="card card--appointment">
  <div class="brand"><span class="brand__dot"></span>Blossom</div>
  <h1 class="appointment__title">Book your Appointment</h1>
  <div class="appointment__form">
    <div class="form-row"><span>Name</span><span class="form-row__blank form-row__blank--grow"></span></div>
    <div class="form-row"><span>(1)</span><span class="form-row__blank form-row__blank--entry"></span><span class="form-row__label--date">Date</span><span class="form-row__blank form-row__blank--date"></span><span class="form-row__label--time">Time</span><span class="form-row__blank form-row__blank--time"></span></div>
    <div class="form-row"><span>(2)</span><span class="form-row__blank form-row__blank--entry"></span><span class="form-row__label--date">Date</span><span class="form-row__blank form-row__blank--date"></span><span class="form-row__label--time">Time</span><span class="form-row__blank form-row__blank--time"></span></div>
    <div class="form-row"><span>(3)</span><span class="form-row__blank form-row__blank--entry"></span><span class="form-row__label--date">Date</span><span class="form-row__blank form-row__blank--date"></span><span class="form-row__label--time">Time</span><span class="form-row__blank form-row__blank--time"></span></div>
    <div class="form-row"><span>(4)</span><span class="form-row__blank form-row__blank--entry"></span><span class="form-row__label--date">Date</span><span class="form-row__blank form-row__blank--date"></span><span class="form-row__label--time">Time</span><span class="form-row__blank form-row__blank--time"></span></div>
  </div>
  <p class="appointment__notice"><strong>This time is reserved just for you.</strong> If you are unable to keep your appointment, please let us know at least <strong>48 HOURS</strong> in advance so that we may schedule a new time for you.</p>
</section>

<section class="card card--contact">
  <div class="brand"><span class="brand__dot"></span>Blossom</div>
  <div class="contact__details">
    <h2 class="contact__name">Marissa Doyle</h2>
    <p class="contact__role">Physiotherapist</p>
    <p class="contact__specialty">Lymphoedema &amp; Oncology Rehabilitation</p>
    <p class="contact__specialty">Continence &amp; Pelvic Floor</p>
    <ul class="contact__list">
      <li class="contact__phone-pair">
        <span><svg viewBox="0 0 16 16" aria-hidden="true"><path d="M1 6c0-3 3-4 7-4s7 1 7 4v1h-4V5.5H5V7H1zM3 8h10l1 6H2z"/></svg>8431 7560</span>
        <span><svg viewBox="0 0 16 16" aria-hidden="true"><path d="M1 6c0-3 3-4 7-4s7 1 7 4v1h-4V5.5H5V7H1zM3 8h10l1 6H2z"/></svg>8431 7564</span>
      </li>
      <li><svg viewBox="0 0 16 16" aria-hidden="true"><path d="M1 3h14v10H1zM2.5 4.5 8 9l5.5-4.5v1.5L8 10.5 2.5 6z"/></svg>info@blossomcarepartners.com.au</li>
      <li><svg viewBox="0 0 16 16" aria-hidden="true"><path d="M8 1a7 7 0 1 0 0 14A7 7 0 0 0 8 1zm-1 2v3.5H3.2A5 5 0 0 1 7 3zm2 0a5 5 0 0 1 3.8 3.5H9zM3.2 9.5H7V13a5 5 0 0 1-3.8-3.5zm5.8 0h3.8A5 5 0 0 1 9 13z"/></svg>www.blossomcarepartners.com.au</li>
      <li><svg viewBox="0 0 16 16" aria-hidden="true"><path d="M8 1a5 5 0 0 0-5 5c0 4 5 9 5 9s5-5 5-9a5 5 0 0 0-5-5zm0 7a2 2 0 1 1 0-4 2 2 0 0 1 0 4z"/></svg>14 Calloway Ave, Bayhaven 3201</li>
    </ul>
  </div>
</section>

</body>
</html>
```